Keyhaven Homes/Real Estate valuation tool

We need a design for our our new Keyhaven Homes valuation tool.

The tool allows users to book a valuation of their house/property with the Keyhaven Homes, after they choose there property they can then complete their details and choose a booking time.

The mock up of the design we want is attached to this project.(Main Screen)

This also needs to be responsive so the design is easy to use on a mobile device.

Target Market(s)

estate agents

Industry/Entity Type

Real Keyhaven Homes

Number of Pages Required

1 page

Requirements
Must have
• Section 2 and 3 greyed out when user is on step 1
• Section 1 and 3 greyed out when user is on step 2
• Section 1 and 2 greyed out when the user is on step 3
• *** Design must be shown for mobile/ipad and desktop
Nice to have
• Clean and Simple
Should not have
• Dark colours

```html
<!DOCTYPE html>
<html lang="en">
<head>
<meta charset="utf-8">
<meta name="viewport" content="width=device-width, initial-scale=1">
<title>Keyhaven Homes – Book Your Valuation Online</title>
<link href="https://fonts.googleapis.com/css2?family=Open+Sans:wght@300;400;600;700;800&display=swap" rel="stylesheet">
<style>
  :root {
    --page-bg: #eef0f2;
    --rule: #d3d7db;
    --heading: #3c4247;
    --brand: #5a9a12;
    --green: #5a9a12;
    --green-tint: #eaf4dc;
    --green-pale: #d9efbd;
    --white: #ffffff;
    --card-head-muted: #e1e4e7;
    --card-body-muted: #e8ebed;
    --field-border-muted: #d2d6da;
    --text-muted: #a7acb1;
    --action-muted: #cadbb6;
    --action-text-muted: #8fa27a;
    --tab-border: #d5d9dd;
    --slot-border: #d5d9dd;
    --slot-text: #6b7075;
    --tab-date: #565b60;
  }
  * { box-sizing: border-box; margin: 0; padding: 0; }
  html, body { min-height: 100%; }
  body {
    background: var(--page-bg);
    font-family: "Open Sans", Arial, sans-serif;
    color: var(--heading);
  }

  /* Header */
  .site-header {
    height: 111px;
    border-bottom: 1px solid var(--rule);
    display: flex; align-items: center; justify-content: center;
  }
  .brand-name {
    color: var(--brand); font-weight: 700; font-size: 30px;
    letter-spacing: 4px; text-transform: uppercase;
  }

  /* Booking area */
  .booking { width: 960px; margin: 0 auto; padding-top: 34px; }
  .page-title {
    height: 30px;
    display: flex; align-items: center; gap: 34px;
    font-weight: 800; font-size: 21px; letter-spacing: 0.3px; white-space: nowrap;
  }
  .page-title::before, .page-title::after {
    content: ""; flex: 1; height: 3px;
    border-top: 1px solid var(--rule); border-bottom: 1px solid var(--rule);
  }
  .steps {
    margin-top: 26px;
    display: grid; grid-template-columns: repeat(3, 312px); gap: 12px;
  }

  /* Step cards */
  .step-card {
    height: 442px; display: flex; flex-direction: column;
    background: var(--card-body-muted);
  }
  .step-head { height: 67px; flex: none; padding: 14px 20px 0; background: var(--card-head-muted); }
  .step-count { font-size: 13px; line-height: 16px; color: var(--text-muted); }
  .step-name { font-size: 19px; line-height: 22px; font-weight: 800; color: var(--text-muted); text-transform: uppercase; }
  .step-body { flex: 1; padding: 0 21px; }

  .step-card--active { background: var(--white); }
  .step-card--active .step-head { background: var(--green); }
  .step-card--active .step-count { color: var(--green-pale); }
  .step-card--active .step-name { color: var(--white); }

  /* Fields */
  .field-label { display: block; font-size: 14px; line-height: 20px; color: var(--text-muted); margin-top: 16px; }
  .field-label:first-child { margin-top: 25px; }
  .field {
    position: relative; height: 46px; margin-top: 18px;
    border: 1px solid var(--field-border-muted);
    padding: 0 14px; line-height: 44px; font-size: 14px; font-weight: 300; color: var(--text-muted);
  }
  .field:first-child { margin-top: 25px; }
  .field-label + .field { margin-top: 7px; }
  .step-card--details .field-label + .field { margin-top: 3px; }
  .step-card--details .field-label:first-child + .field { margin-top: 7px; }
  .field svg { position: absolute; right: 18px; top: 12px; }

  /* Actions */
  .step-action {
    height: 67px; flex: none;
    background: var(--action-muted);
    display: flex; align-items: center; justify-content: center; gap: 10px;
    font-size: 17px; font-weight: 300; color: var(--action-text-muted); letter-spacing: 0.3px;
  }
  .step-card--active .step-action { background: var(--green); color: var(--white); font-weight: 400; }

  /* Appointment picker */
  .day-tabs { margin-top: 29px; display: flex; gap: 5px; }
  .day-tab {
    width: 34px; height: 34px; border: 1px solid var(--tab-border);
    display: flex; flex-direction: column; align-items: center; justify-content: center;
    font-size: 7.5px; line-height: 9px; font-weight: 600; color: var(--tab-date);
  }
  .day-tab .day { color: var(--green); }
  .day-tab--current { background: var(--green); border-color: var(--green); }
  .day-tab--current .day { color: var(--white); }
  .slot-list { margin-top: 12px; display: flex; flex-direction: column; gap: 10px; }
  .slot { height: 35px; display: flex; }
  .slot-date {
    flex: 1; border: 1px solid var(--slot-border); border-right: none;
    padding-left: 13px; line-height: 33px; font-size: 14px; font-weight: 600; color: var(--slot-text);
  }
  .slot-time {
    width: 78px; background: var(--green-tint); color: var(--green);
    font-size: 14px; font-weight: 700; text-align: center; line-height: 35px;
  }

  /* Desktop canvas: fixed, no scrolling */
  @media (min-width: 1024px) {
    html, body { height: 664px; overflow: hidden; }
  }

  /* Tablet */
  @media (max-width: 1023px) {
    .booking { width: auto; padding: 34px 32px 40px; }
    .steps { grid-template-columns: 1fr 1fr; }
    .step-card--active { grid-column: 1 / -1; }
    .step-card { height: auto; }
    .step-body { padding-bottom: 26px; }
    .day-tabs { flex-wrap: wrap; }
    .day-tab { flex: 1; min-width: 34px; }
  }

  /* Mobile */
  @media (max-width: 640px) {
    .site-header { height: 80px; }
    .brand-name { font-size: 22px; letter-spacing: 3px; }
    .booking { padding: 24px 16px 32px; }
    .page-title { font-size: 17px; gap: 14px; }
    .steps { grid-template-columns: 1fr; margin-top: 20px; }
    .day-tab { height: 40px; font-size: 9px; line-height: 11px; }
    .slot { height: 44px; }
    .slot-date { line-height: 42px; }
    .slot-time { line-height: 44px; }
  }
</style>
</head>
<body>
  <header class="site-header">
    <div class="brand-name">Keyhaven Homes</div>
  </header>

  <main class="booking">
    <h1 class="page-title">BOOK YOUR VALUATION ONLINE</h1>

    <div class="steps">
      <section class="step-card step-card--property">
        <div class="step-head">
          <div class="step-count">STEP 1 OF 3</div>
          <div class="step-name">Property Details</div>
        </div>
        <div class="step-body">
          <label class="field-label">Postcode</label>
          <div class="field">123
            <svg width="20" height="20" viewBox="0 0 20 20" fill="none" stroke="#a7acb1" stroke-width="2.4"><circle cx="8" cy="8" r="6"/><path d="M12.5 12.5 L18 18"/></svg>
          </div>
          <div class="field" style="margin-top:17px">123 Test Street</div>
          <div class="field">Test City</div>
          <div class="field" style="margin-top:19px">Test Country</div>
        </div>
        <div class="step-action">PROCEED
          <svg width="22" height="22" viewBox="0 0 22 22"><circle cx="11" cy="11" r="11" fill="#8fa27a"/><path d="M8.5 6.5 L15.5 11 L8.5 15.5 Z" fill="#cadbb6"/></svg>
        </div>
      </section>

      <section class="step-card step-card--details">
        <div class="step-head">
          <div class="step-count">STEP 2 OF 3</div>
          <div class="step-name">Your Details</div>
        </div>
        <div class="step-body">
          <label class="field-label">Your Name</label>
          <div class="field"></div>
          <label class="field-label">Your Email</label>
          <div class="field"></div>
          <label class="field-label" style="margin-top:17px">Your Contact Number</label>
          <div class="field" style="margin-top:4px"></div>
        </div>
        <div class="step-action">PROCEED
          <svg width="22" height="22" viewBox="0 0 22 22"><circle cx="11" cy="11" r="11" fill="#8fa27a"/><path d="M8.5 6.5 L15.5 11 L8.5 15.5 Z" fill="#cadbb6"/></svg>
        </div>
      </section>

      <section class="step-card step-card--time step-card--active">
        <div class="step-head">
          <div class="step-count">STEP 3 OF 3</div>
          <div class="step-name">Appointment Time</div>
        </div>
        <div class="step-body">
          <div class="day-tabs">
            <div class="day-tab"><span class="day">TODAY</span></div>
            <div class="day-tab day-tab--current"><span class="day">TOM</span></div>
            <div class="day-tab"><span class="day">MON</span><span>30th</span></div>
            <div class="day-tab"><span class="day">TUE</span><span>1st</span></div>
            <div class="day-tab"><span class="day">WED</span><span>2nd</span></div>
            <div class="day-tab"><span class="day">THURS</span><span>3rd</span></div>
            <div class="day-tab"><span class="day">FRI</span><span>4th</span></div>
          </div>
          <div class="slot-list">
            <div class="slot"><div class="slot-date">Sunday 29th November</div><div class="slot-time">08:30</div></div>
            <div class="slot"><div class="slot-date">Sunday 29th November</div><div class="slot-time">08:30</div></div>
            <div class="slot"><div class="slot-date">Sunday 29th November</div><div class="slot-time">08:30</div></div>
            <div class="slot"><div class="slot-date">Sunday 29th November</div><div class="slot-time">08:30</div></div>
            <div class="slot"><div class="slot-date">Sunday 29th November</div><div class="slot-time">08:30</div></div>
          </div>
        </div>
        <div class="step-action">CONFIRM BOOKING
          <svg width="26" height="26" viewBox="0 0 26 26"><circle cx="13" cy="13" r="13" fill="#ffffff"/><path d="M10 7.5 L18 13 L10 18.5 Z" fill="#5a9a12"/></svg>
        </div>
      </section>
    </div>
  </main>
</body>
</html>
```